Brookmere Roofing Business Card

This is my current business card. But I’d like to make some changes. Somewhere on the card I’d like to list some of the services we offer. Maybe on the back? But I’d still like to keep the red. White and black modern look.

-residential & commercial roofing
-Roof Repairs & Maintenance
-Storm Damage & Insurance Claims specialist
-Christmas Lights and permanent Christmas lights
Fencing. Windows. Gutters. Siding. Sheetrock, painting.

```html
<!DOCTYPE html>
<html lang="en">
<head>
<meta charset="utf-8">
<title>Brookmere Roofing Business Card</title>
<link rel="stylesheet" href="https://fonts.googleapis.com/css2?family=Michroma&family=Oswald:wght@300;400&display=swap">
<style>
  :root {
    --stage: #979797;
    --white: #ffffff;
    --red: #e31e26;
    --deep-red: #8f181c;
    --black: #0c0c0c;
    --stripe: #2a2a2a;
    --ink: #3d3d3d;
    --rule: #7a7a7a;
  }
  * { box-sizing: border-box; margin: 0; padding: 0; }
  html, body { width: 1200px; height: 1000px; overflow: hidden; }
  body { background: var(--stage); position: relative; font-family: "Oswald", sans-serif; }

  .card {
    position: absolute; left: 252px; width: 694px; height: 400px;
    border-radius: 24px; overflow: hidden;
    box-shadow: 0 14px 30px rgba(0,0,0,0.35);
  }
  .card--front { top: 72px; background: var(--white); }
  .card--back { top: 514px; background: var(--deep-red); }

  /* front */
  .brand { position: absolute; left: 55px; top: 63px; display: flex; align-items: center; gap: 10px; }
  .brand__dot { width: 62px; height: 62px; border-radius: 50%; background: var(--red); }
  .brand__name {
    font-family: "Michroma", sans-serif; color: var(--red);
    font-size: 19px; line-height: 22px; letter-spacing: 0.5px;
  }
  .person { position: absolute; left: 60px; width: 256px; top: 162px; text-align: center; }
  .person__name { font-family: "Michroma", sans-serif; font-size: 18px; color: var(--black); letter-spacing: 1px; }
  .person__name em { font-style: normal; color: var(--red); }
  .person__role { font-family: "Michroma", sans-serif; font-size: 11px; color: var(--ink); letter-spacing: 4px; margin-top: 4px; }
  .contact-icons { position: absolute; left: 76px; top: 220px; width: 226px; display: flex; align-items: center; gap: 7px; }
  .contact-icons__rule { flex: 1; height: 2px; background: var(--rule); }
  .contact-icons svg { width: 25px; height: 25px; }
  .contact { position: absolute; left: 40px; width: 296px; top: 254px; text-align: center; color: var(--ink); font-weight: 300; font-size: 23px; line-height: 29px; }
  .emblem { position: absolute; left: 0; top: 0; }

  /* back */
  .back-art { position: absolute; left: 0; top: 0; }
  .services {
    position: absolute; right: 66px; top: 94px; text-align: right;
    color: var(--white); font-weight: 300; font-size: 30px; line-height: 37px;
    list-style: none;
  }
</style>
</head>
<body>

<section class="card card--front">
  <svg class="emblem" width="694" height="400" viewBox="0 0 694 400" role="img" aria-label="Large brand mascot emblem on a red disc">
    <circle cx="660" cy="232" r="276" fill="var(--deep-red)"/>
  </svg>

  <div class="brand">
    <div class="brand__dot"></div>
    <div class="brand__name">BROOKMERE<br>ROOFING CO.</div>
  </div>

  <div class="person">
    <div class="person__name">DEAN <em>CARVER</em></div>
    <div class="person__role">OWNER</div>
  </div>

  <div class="contact-icons">
    <span class="contact-icons__rule"></span>
    <svg viewBox="0 0 24 24" aria-label="Phone"><circle cx="12" cy="12" r="12" fill="var(--red)"/><path d="M8.5 6.5l2 2.3-1.1 1.4c.8 1.7 2 2.9 3.7 3.7l1.4-1.1 2.3 2-1.2 1.9c-4.2-.4-7.6-3.8-8-8z" fill="#fff"/></svg>
    <svg viewBox="0 0 24 24" aria-label="Email"><circle cx="12" cy="12" r="12" fill="var(--red)"/><rect x="6.5" y="8" width="11" height="8" fill="none" stroke="#fff" stroke-width="1.5"/><path d="M6.5 8l5.5 4.5L17.5 8" fill="none" stroke="#fff" stroke-width="1.5"/></svg>
    <svg viewBox="0 0 24 24" aria-label="Website"><circle cx="12" cy="12" r="12" fill="var(--red)"/><g fill="none" stroke="#fff" stroke-width="1.3"><circle cx="12" cy="12" r="5.8"/><ellipse cx="12" cy="12" rx="2.5" ry="5.8"/><path d="M6.2 12h11.6M7 9h10M7 15h10"/></g></svg>
    <span class="contact-icons__rule"></span>
  </div>

  <div class="contact">
    <div>682-555-0147</div>
    <div>dean@brookmereroofing.com</div>
    <div>brookmereroofing.com</div>
  </div>
</section>

<section class="card card--back">
  <svg class="back-art" width="694" height="400" viewBox="0 0 694 400">
    <defs>
      <clipPath id="stripe-zone"><rect x="0" y="0" width="119" height="400"/></clipPath>
    </defs>
    <rect x="432" y="0" width="262" height="400" fill="var(--red)"/>
    <rect x="0" y="0" width="432" height="37" fill="var(--red)"/>
    <rect x="432" y="0" width="262" height="37" fill="var(--black)"/>
    <g clip-path="url(#stripe-zone)" stroke="var(--stripe)" stroke-width="20">
      <line x1="20" y1="-70" x2="160" y2="70"/>
      <line x1="-60" y1="-20" x2="160" y2="200"/>
      <line x1="-60" y1="65" x2="160" y2="285"/>
      <line x1="-60" y1="150" x2="160" y2="370"/>
      <line x1="-60" y1="235" x2="160" y2="455"/>
      <line x1="-60" y1="320" x2="160" y2="540"/>
    </g>
  </svg>
  <ul class="services">
    <li>Residential &amp; Commercial Roofing</li>
    <li>Roof Repairs &amp; Maintenance</li>
    <li>Storm Damage &amp; Insurance Claims</li>
    <li>Specialist Christmas Lights and</li>
    <li>Permanent Christmas Lights</li>
    <li>Fencing • Windows • Gutters</li>
    <li>Siding • Sheetrock • Painting</li>
  </ul>
</section>

</body>
</html>
```